New Business Card Design Project

Details for my new Business Card Design Project will be added soon. Like a nice simple design

Target Market(s)

Home improvement

Industry/Entity Type

Home Improvement

Contact Information for Business Card

Roofing siding gutters additions garages decks

Requirements
Must have
• Phone 5074629183
• Email morvantgc@quellmail.com

```html
<!DOCTYPE html>
<html lang="en">
<head>
<meta charset="utf-8">
<title>Morvant Contracting – Business Card</title>
<link rel="stylesheet" href="https://fonts.googleapis.com/css2?family=Open+Sans:wght@400;600;700&display=swap">
<style>
  :root {
    --page-bg: #e9eaec;
    --card-white: #ffffff;
    --brand-blue: #1f5fa6;
    --brand-blue-dark: #174c88;
    --text-blue: #2f6aa8;
    --text-white: #ffffff;
  }
  html, body {
    margin: 0;
    width: 1200px;
    height: 1023px;
    overflow: hidden;
    background: var(--page-bg);
    font-family: "Open Sans", Arial, sans-serif;
  }
  .card {
    position: absolute;
    left: 100px;
    top: 226px;
    width: 1000px;
    height: 571px;
    background: var(--card-white);
    border-radius: 22px;
    overflow: hidden;
    box-shadow: 0 10px 30px rgba(0, 0, 0, 0.18);
  }
  .card-band {
    position: absolute;
    inset: 0;
    width: 100%;
    height: 100%;
  }
  .brand {
    position: absolute;
    left: 64px;
    top: 70px;
    display: flex;
    align-items: center;
    gap: 14px;
    color: var(--brand-blue);
    font-weight: 700;
    font-size: 34px;
    letter-spacing: 0.5px;
  }
  .brand-mark {
    width: 20px;
    height: 20px;
    background: var(--brand-blue);
  }
  .contact {
    position: absolute;
    left: 250px;
    top: 320px;
    color: var(--text-blue);
  }
  .contact-name {
    margin: 0 0 16px;
    font-size: 38px;
    font-weight: 700;
  }
  .contact-list {
    list-style: none;
    margin: 0;
    padding: 0;
    font-size: 25px;
    line-height: 1.55;
  }
  .contact-list li {
    display: flex;
    align-items: center;
    gap: 14px;
  }
  .contact-icon {
    width: 20px;
    height: 20px;
    flex: none;
  }
  .services {
    position: absolute;
    right: 48px;
    top: 54px;
    color: var(--text-white);
    text-align: right;
  }
  .services-title {
    margin: 0 0 10px;
    padding: 0 20px 6px 40px;
    font-size: 24px;
    font-weight: 700;
    border-bottom: 2px solid var(--text-white);
    display: inline-block;
  }
  .services-list {
    list-style: none;
    margin: 0;
    padding: 0;
    font-size: 24px;
    line-height: 1.45;
  }
  .services-list li::after {
    content: "";
    display: inline-block;
    width: 7px;
    height: 7px;
    margin-left: 12px;
    border-radius: 50%;
    background: var(--text-white);
    vertical-align: middle;
  }
  .services-list .services-spaced {
    margin-top: 40px;
  }
</style>
</head>
<body>
  <article class="card">
    <svg class="card-band" viewBox="0 0 1000 571" aria-hidden="true">
      <polygon points="770,0 1000,0 1000,571 770,571 630,285" fill="var(--brand-blue-dark)"/>
      <polygon points="800,0 1000,0 1000,571 800,571 660,285" fill="var(--card-white)"/>
      <polygon points="830,0 1000,0 1000,571 830,571 690,285" fill="var(--brand-blue)"/>
    </svg>

    <div class="brand">
      <span class="brand-mark"></span>
      <span class="brand-name">Morvant Contracting</span>
    </div>

    <section class="contact">
      <h1 class="contact-name">Your Name</h1>
      <ul class="contact-list">
        <li>
          <svg class="contact-icon" viewBox="0 0 20 20"><circle cx="10" cy="10" r="8.5" fill="none" stroke="currentColor" stroke-width="1.8"/><path d="M7 6.5c0 4 2.5 7 6.5 7l.5-2-2-1-1 1c-1.3-.6-2.300-1.600-2.900-2.900l1-1-1-2z" fill="currentColor"/></svg>
          5074629183
        </li>
        <li>
          <svg class="contact-icon" viewBox="0 0 20 20"><rect x="1.5" y="4" width="17" height="12" fill="currentColor"/><path d="M1.5 4l8.5 7 8.5-7" fill="none" stroke="#fff" stroke-width="1.5"/></svg>
          morvantgc@quellmail.com
        </li>
        <li>
          <svg class="contact-icon" viewBox="0 0 20 20" fill="none" stroke="currentColor" stroke-width="1.5"><circle cx="10" cy="10" r="8.5"/><ellipse cx="10" cy="10" rx="3.8" ry="8.5"/><path d="M1.5 10h17M3 5.5h14M3 14.5h14"/></svg>
          www.yourweb.com
        </li>
      </ul>
    </section>

    <section class="services">
      <h2 class="services-title">We Offer</h2>
      <ul class="services-list">
        <li>Roofing</li>
        <li>Siding</li>
        <li>Gutter</li>
        <li>Additions</li>
        <li>Decks</li>
        <li class="services-spaced">Handyman Services</li>
      </ul>
    </section>
  </article>
</body>
</html>
```